Solar Advertising Flier to generate Biz

I need a advertisement that generates business to be used in a mailer for marketing purposes.

Im attaching a file that is a an idea of advertisement.
I do not want the "ZVN" specific information on it.
I want the background solar panels.
Same information as the ad.
And I've attached my Logo - I want the color scheme to match this.

Thank you

Target Market(s)

Middle to Upper Class Home Owners

Industry/Entity Type

Solar Energy

Requirements
Must have
• A call to action
• A professional look
Nice to have
• A family
• Great looking solar panels
Should not have
• Cartoons

```html
<!DOCTYPE html>
<html lang="en">
<head>
<meta charset="utf-8">
<title>Go Solar Flier</title>
<link rel="stylesheet" href="https://fonts.googleapis.com/css2?family=Archivo+Black&family=Roboto:wght@400;700;900&display=swap">
<style>
  :root {
    --page-bg: #e9eaec;
    --sky-top: #2f8fd6;
    --sky-mid: #8cc3ec;
    --sky-light: #eef5fb;
    --brand-blue: #1a86c9;
    --panel-blue: #2a62b8;
    --panel-dark: #173f86;
    --brand-green: #8cc63f;
    --text-dark: #1b1b1b;
    --white: #ffffff;
  }
  * { box-sizing: border-box; margin: 0; padding: 0; }
  html, body { width: 1200px; height: 898px; overflow: hidden; }
  body {
    background: var(--page-bg);
    font-family: "Roboto", Arial, sans-serif;
    position: relative;
  }
  .flier {
    position: absolute;
    left: 300px; top: 25px;
    width: 600px; height: 848px;
    overflow: hidden;
    background: var(--sky-light);
    box-shadow: 0 6px 18px rgba(0,0,0,0.18);
  }
  .sky-photo {
    position: absolute; inset: 0 0 35% 0;
    background:
      radial-gradient(ellipse 45% 22% at 40% 22%, rgba(255,255,255,0.95), rgba(255,255,255,0) 70%),
      radial-gradient(ellipse 40% 20% at 75% 38%, rgba(255,255,255,0.9), rgba(255,255,255,0) 70%),
      linear-gradient(180deg, var(--sky-top) 0%, var(--sky-mid) 35%, var(--sky-light) 75%);
  }
  .panel-photo {
    position: absolute; left: 0; right: 0; bottom: 0; height: 42%;
    background: linear-gradient(170deg, #5d8fd6 0%, var(--panel-blue) 40%, var(--panel-dark) 100%);
  }
  .brand {
    position: absolute; top: 62px; left: 0; right: 0;
    display: flex; align-items: center; justify-content: center; gap: 10px;
  }
  .brand-dot {
    width: 22px; height: 22px; border-radius: 50%;
    background: var(--brand-green);
  }
  .brand-name {
    font-weight: 700; font-size: 24px; letter-spacing: 1px;
    color: var(--brand-blue);
  }
  .headline {
    position: absolute; top: 118px; left: 0; right: 0;
    text-align: center; white-space: nowrap;
    font-family: "Archivo Black", Arial, sans-serif;
    font-size: 88px; line-height: 1;
    color: var(--white);
    -webkit-text-stroke: 6px var(--brand-blue);
    paint-order: stroke fill;
    text-shadow: 0 4px 6px rgba(0,0,0,0.25);
  }
  .subhead {
    position: absolute; top: 226px; left: 0; right: 0;
    text-align: center; white-space: nowrap;
    font-weight: 900; font-size: 18px;
    color: var(--brand-blue);
  }
  .benefits {
    position: absolute; top: 260px; left: 60px; right: 50px;
    list-style: none;
    border-top: 1px solid var(--brand-blue);
  }
  .benefit {
    display: flex; align-items: center; gap: 18px;
    height: 56px;
    border-bottom: 1px solid var(--brand-blue);
    font-weight: 700; font-size: 16px; line-height: 1.2;
    color: var(--text-dark);
  }
  .benefit svg { flex: 0 0 38px; }
  .how-box {
    position: absolute; top: 532px; left: 45px; right: 55px;
    background: var(--brand-green);
    border: 3px solid var(--white);
    border-radius: 14px;
    padding: 30px 22px 18px;
    color: var(--white);
    font-size: 16px; line-height: 1.35;
  }
  .how-box strong { font-weight: 900; }
  .how-title {
    position: absolute; top: -22px; left: 14px;
    font-weight: 900; font-size: 28px;
    color: var(--brand-blue);
    -webkit-text-stroke: 5px var(--white);
    paint-order: stroke fill;
  }
  .how-tail {
    position: absolute; right: 40px; bottom: -22px;
    width: 0; height: 0;
    border-left: 24px solid transparent;
    border-top: 22px solid var(--brand-green);
  }
  .call-bar {
    position: absolute; top: 712px; left: 45px; right: 55px;
    height: 92px;
    background: var(--white);
    border: 4px solid var(--brand-blue);
    border-radius: 46px;
    display: flex; align-items: center; gap: 20px;
    padding-left: 12px;
  }
  .call-icon {
    width: 66px; height: 66px; border-radius: 50%;
    background: var(--brand-blue);
    display: flex; align-items: center; justify-content: center;
  }
  .call-text { font-family: "Archivo Black", Arial, sans-serif; line-height: 1; }
  .call-cta {
    font-size: 30px; color: var(--brand-green);
    -webkit-text-stroke: 3px var(--text-dark);
    paint-order: stroke fill;
  }
  .call-number { font-size: 42px; color: var(--text-dark); }
</style>
</head>
<body>
  <article class="flier">
    <div class="sky-photo" role="img" aria-label="Bright blue sky with white clouds"></div>
    <div class="panel-photo" role="img" aria-label="Rooftop solar panels in close view"></div>

    <header class="brand">
      <span class="brand-dot"></span>
      <span class="brand-name">BRIGHT HORIZON ENERGY</span>
    </header>

    <h1 class="headline">GO SOLAR</h1>
    <p class="subhead">GET GRANDFATHERED BEFORE THE NEW DEADLINE</p>

    <ul class="benefits">
      <li class="benefit">
        <svg width="38" height="38" viewBox="0 0 38 38"><circle cx="19" cy="19" r="15" fill="none" stroke="#1a86c9" stroke-width="3"/><text x="19" y="26" text-anchor="middle" font-family="Arial" font-weight="bold" font-size="20" fill="#8cc63f">$</text><line x1="8" y1="30" x2="30" y2="8" stroke="#1a86c9" stroke-width="3"/></svg>
        <span>$0 Down, no upfront cost.</span>
      </li>
      <li class="benefit">
        <svg width="38" height="38" viewBox="0 0 38 38"><path d="M6 30 L18 12 L24 20 L32 8" fill="none" stroke="#8cc63f" stroke-width="4" stroke-linejoin="round"/><path d="M26 8 L33 7 L32 14" fill="none" stroke="#8cc63f" stroke-width="4"/><circle cx="14" cy="28" r="7" fill="#1a86c9"/><text x="14" y="32" text-anchor="middle" font-family="Arial" font-weight="bold" font-size="11" fill="#fff">$</text></svg>
        <span>Save up to 90% off your utility bill.</span>
      </li>
      <li class="benefit">
        <svg width="38" height="38" viewBox="0 0 38 38"><rect x="4" y="14" width="20" height="14" fill="none" stroke="#1a86c9" stroke-width="3"/><circle cx="29" cy="13" r="6" fill="none" stroke="#8cc63f" stroke-width="3"/><path d="M6 32 L11 36 L20 26" fill="none" stroke="#8cc63f" stroke-width="3"/></svg>
        <span>Protect against inflation &amp; energy costs increases from your Utility Company.</span>
      </li>
      <li class="benefit">
        <svg width="38" height="38" viewBox="0 0 38 38"><rect x="4" y="10" width="26" height="16" fill="#1a86c9"/><path d="M4 18 H30 M13 10 V26 M22 10 V26" stroke="#fff" stroke-width="1.5"/><rect x="28" y="20" width="8" height="12" fill="#8cc63f"/></svg>
        <span>Provide clean, reliable energy for your family powered by the sun.</span>
      </li>
    </ul>

    <section class="how-box">
      <h2 class="how-title">How it works...</h2>
      <p>Your solar system allows you to generate your own clean power and <strong>COSTS LESS</strong> than your current utility company. Simply pay by the month, like you do know... but at a <strong>LOWER</strong> rate and <strong>START SAVING IMMEDIATELY</strong>.</p>
      <span class="how-tail"></span>
    </section>

    <section class="call-bar">
      <div class="call-icon">
        <svg width="34" height="34" viewBox="0 0 24 24"><path fill="#fff" d="M6.6 10.8a15 15 0 0 0 6.6 6.6l2.2-2.2a1 1 0 0 1 1-.25 11.4 11.4 0 0 0 3.6.57 1 1 0 0 1 1 1V20a1 1 0 0 1-1 1A17 17 0 0 1 3 4a1 1 0 0 1 1-1h3.5a1 1 0 0 1 1 1c0 1.25.2 2.45.57 3.57a1 1 0 0 1-.25 1z"/></svg>
      </div>
      <div class="call-text">
        <div class="call-cta">CALL US TODAY</div>
        <div class="call-number">123 456 789</div>
      </div>
    </section>
  </article>
</body>
</html>
```